Construction business card

I need a new business card, they can connect with my logo, brand.
What we do is residential house , design and build
I like: Navy blue / black
I attached our logo, brand,
and, some idea for business card.

```html
<!DOCTYPE html>
<html lang="en">
<head>
<meta charset="utf-8">
<title>Harlow Building Group – Business Card</title>
<link href="https://fonts.googleapis.com/css2?family=Lato:wght@400;700;900&display=swap" rel="stylesheet">
<style>
  :root {
    --backdrop: #262626;
    --card: #070707;
    --brand-blue: #3b86f2;
    --white: #ffffff;
    --text-light: #ececec;
  }
  * { box-sizing: border-box; margin: 0; padding: 0; }
  html, body {
    width: 1200px; height: 1200px; overflow: hidden;
    background: var(--backdrop);
    font-family: "Lato", sans-serif;
  }
  .canvas { position: relative; width: 1200px; height: 1200px; }
  .card {
    position: absolute; left: 270px; width: 688px; height: 394px;
    background: var(--card); border-radius: 26px;
  }
  .card--front { top: 194px; }
  .card--back { top: 618px; }

  .brand {
    display: flex; align-items: center; gap: 10px;
    color: var(--white); font-weight: 900; text-transform: uppercase;
    letter-spacing: 0.04em; line-height: 1.1;
  }
  .brand__mark { background: var(--brand-blue); flex: none; }
  .card--front .brand {
    position: absolute; right: 50px; top: 92px; font-size: 20px;
  }
  .card--front .brand__mark { width: 18px; height: 18px; }
  .card--back .brand {
    position: absolute; left: 0; right: 0; top: 172px;
    justify-content: center; font-size: 38px; gap: 16px;
  }
  .card--back .brand__mark { width: 34px; height: 34px; }

  .person { position: absolute; left: 50px; top: 190px; }
  .person__name {
    color: var(--brand-blue); font-size: 27px; font-weight: 700;
    text-transform: uppercase; letter-spacing: 0.01em;
  }
  .person__role { color: var(--text-light); font-size: 18px; margin-top: 8px; }

  .divider {
    position: absolute; left: 54px; right: 50px; top: 264px;
    height: 1.5px; background: var(--text-light);
  }

  .contacts { position: absolute; left: 54px; top: 277px; list-style: none; }
  .contacts li {
    display: flex; align-items: center; gap: 18px;
    height: 31px; color: var(--text-light); font-size: 18.5px;
  }
  .contacts svg { width: 20px; height: 20px; fill: var(--brand-blue); flex: none; }

  .address {
    position: absolute; right: 50px; top: 299px;
    text-align: right; color: var(--text-light);
    font-size: 18.5px; line-height: 26px; font-style: normal;
  }
</style>
</head>
<body>
<main class="canvas">

  <section class="card card--front">
    <div class="brand"><span class="brand__mark"></span>Harlow Building Group</div>

    <div class="person">
      <h1 class="person__name">Marcus Reilly</h1>
      <p class="person__role">Owner</p>
    </div>

    <div class="divider"></div>

    <ul class="contacts">
      <li>
        <svg viewBox="0 0 24 24" aria-hidden="true"><path d="M6.6 10.8a15.1 15.1 0 0 0 6.6 6.6l2.2-2.2a1 1 0 0 1 1-.25 11.4 11.4 0 0 0 3.6.57 1 1 0 0 1 1 1V20a1 1 0 0 1-1 1A17 17 0 0 1 3 4a1 1 0 0 1 1-1h3.5a1 1 0 0 1 1 1c0 1.25.2 2.45.57 3.57a1 1 0 0 1-.25 1z"/></svg>
        0412 555 308
      </li>
      <li>
        <svg viewBox="0 0 24 24" aria-hidden="true"><path d="M2 5h20v2l-10 6L2 7z M2 9l10 6 10-6v10H2z"/></svg>
        hello@harlowbuild.com
      </li>
      <li>
        <svg viewBox="0 0 24 24" aria-hidden="true"><path d="M12 2a10 10 0 1 0 0 20 10 10 0 0 0 0-20zm-1 17.9A8 8 0 0 1 4.1 10.8L9 15.7v1.1a2 2 0 0 0 2 2zm6.9-2.5A2 2 0 0 0 16 16h-1v-3a1 1 0 0 0-1-1H8v-2h2a1 1 0 0 0 1-1V7h2a2 2 0 0 0 2-2v-.4a8 8 0 0 1 2.9 12.8z"/></svg>
        www.harlowbuild.com
      </li>
    </ul>

    <address class="address">28 Elmstead Avenue,<br>Kingsford, Vic 3061</address>
  </section>

  <section class="card card--back">
    <div class="brand"><span class="brand__mark"></span>Harlow Building Group</div>
  </section>

</main>
</body>
</html>
```